Billboard Design

Billboard design featuring the colors dark teal and dark grey.
Company: Juniper Crest Holdings
Services Real Estate & Management
Phone: 717-390-6158
Important info:
Professionalizing Property Management
Specialized training and credentials in Property Management
Serving single family, multifamily, complexes, and mixed use properties.

UPDATE: We have uploaded photos from a recent project of ours and would love to see them used on the billboard.

```html
<!DOCTYPE html>
<html lang="en">
<head>
<meta charset="utf-8">
<title>Juniper Crest Holdings Billboard</title>
<link href="https://fonts.googleapis.com/css2?family=Great+Vibes&family=Marcellus&family=Roboto:wght@400;700&display=swap" rel="stylesheet">
<style>
  :root {
    --page-bg: #e6e6e6;
    --teal: #2a7371;
    --slate: #545456;
    --white: #ffffff;
    --ink: #222222;
    --photo-sky: #b9cfe0;
    --photo-house: #a48a6e;
    --photo-lawn: #6f8f3e;
  }
  html, body {
    margin: 0;
    padding: 0;
    width: 934px;
    height: 1200px;
    overflow: hidden;
    background: var(--page-bg);
  }
  .billboard {
    position: absolute;
    left: 27px;
    top: 470px;
    width: 880px;
    height: 259px;
    box-shadow: 0 3px 6px rgba(0,0,0,0.35);
  }
  .billboard svg { display: block; width: 100%; height: 100%; }
  .brand-script { font-family: "Great Vibes", cursive; fill: var(--white); }
  .brand-caps { font-family: "Marcellus", serif; fill: var(--white); }
  .phone-number { font-family: "Roboto", sans-serif; font-weight: 700; fill: var(--white); }
  .service-line { font-family: "Roboto", sans-serif; font-weight: 400; fill: var(--white); }
  .feature-text { font-family: "Roboto", sans-serif; font-weight: 400; fill: var(--white); }
  .badge-name { font-family: "Roboto", sans-serif; font-weight: 400; fill: var(--ink); }
</style>
</head>
<body>
  <div class="billboard">
    <svg viewBox="0 0 1264 372" xmlns="http://www.w3.org/2000/svg">
      <defs>
        <linearGradient id="photo-tones" x1="0" y1="0" x2="0" y2="1">
          <stop offset="0" stop-color="var(--photo-sky)"/>
          <stop offset="0.3" stop-color="var(--photo-house)"/>
          <stop offset="0.8" stop-color="var(--photo-house)"/>
          <stop offset="1" stop-color="var(--photo-lawn)"/>
        </linearGradient>
      </defs>

      <rect class="base-panel" width="1264" height="372" fill="var(--slate)"/>

      <path class="project-photo" role="img" aria-label="Photo of a recent project: two-storey brick house with lawn"
            d="M0,0 H368 C356,60 354,120 360,176 L0,238 Z" fill="url(#photo-tones)"/>

      <path class="teal-band"
            d="M368,0 H1264 V65 C1180,140 1060,200 920,200 C860,200 800,195 720,185 C600,172 480,165 360,176 C354,120 356,60 368,0 Z"
            fill="var(--teal)"/>

      <path class="white-swoosh"
            d="M360,176 C480,165 600,172 720,185 C800,195 860,200 920,200 C1060,200 1180,140 1264,65 V112 C1180,190 1060,228 920,228 C860,228 800,218 720,205 C600,185 480,172 360,180 Z"
            fill="var(--white)"/>

      <text class="brand-script" x="565" y="76" font-size="54" text-anchor="middle">Juniper Crest</text>
      <text class="brand-caps" x="567" y="130" font-size="50" text-anchor="middle">HOLDINGS</text>

      <path class="phone-icon" fill="var(--white)"
            d="M805,22 l12,-3 l8,18 l-8,6 c4,9 10,15 18,19 l6,-8 l18,8 l-3,12 c-2,5 -6,6 -10,6 c-24,-3 -42,-22 -45,-46 c0,-5 1,-9 4,-12 z"/>
      <text class="phone-number" x="845" y="67" font-size="57" textLength="352" lengthAdjust="spacingAndGlyphs">717-390-6158</text>
      <rect class="phone-rule" x="798" y="76" width="394" height="2" fill="var(--white)"/>
      <text class="service-line" x="1002" y="106" font-size="24" text-anchor="middle">REAL ESTATE &amp; MANAGEMENT</text>

      <g class="feature-list">
        <circle cx="47" cy="265" r="8" fill="var(--white)"/>
        <text class="feature-text" x="67" y="275" font-size="29">Professionalizing Property Management</text>
        <circle cx="47" cy="300" r="8" fill="var(--white)"/>
        <text class="feature-text" x="67" y="310" font-size="29">Specialized training and credentials in Property Management</text>
        <circle cx="47" cy="338" r="8" fill="var(--white)"/>
        <text class="feature-text" x="65" y="348" font-size="29" textLength="948" lengthAdjust="spacingAndGlyphs">Serving single family, multifamily, complexes, and mixed use properties.</text>
      </g>

      <g class="name-badge">
        <rect x="1054" y="293" width="189" height="62" fill="var(--white)" stroke="var(--ink)" stroke-width="1.5"/>
        <rect x="1064" y="313" width="20" height="20" fill="var(--teal)"/>
        <text class="badge-name" x="1092" y="320" font-size="15">Juniper Crest</text>
        <text class="badge-name" x="1092" y="338" font-size="15">Holdings</text>
      </g>
    </svg>
  </div>
</body>
</html>
```